Northfield Builders Guild Business card

We are looking for a new business card design with photo included.
Our business is a nonprofit construction contractor membership organization. We offer business education, assist with business setup and licensing, provide safety training, and provide a member directory.
URL: www.brickwayguildnetwork.org
Color code:
CMYK: 0 cyan, 42 magenta, 100 yellow, 0 black for Print.
Hexidecimal: #FF9900
RGB: R 255; G 153; B 0

```html
<!DOCTYPE html>
<html lang="en">
<head>
<meta charset="utf-8">
<title>Northfield Builders Guild – Business Card</title>
<link rel="stylesheet" href="https://fonts.googleapis.com/css2?family=Arimo:wght@400;700&display=swap">
<style>
  :root {
    --page-bg: #e9e6e3;
    --card-dark: #1d1d1f;
    --brand-orange: #f7991c;
    --text-light: #ffffff;
    --logo-dark: #2b2b2d;
    --window-top: #f1e9e7;
    --window-bottom: #cfc6c4;
  }
  * { box-sizing: border-box; margin: 0; padding: 0; }
  html, body {
    width: 1200px; height: 900px; overflow: hidden;
    background: var(--page-bg);
    font-family: "Arimo", Arial, sans-serif;
  }
  .card {
    position: absolute; left: 100px; top: 140px;
    width: 1000px; height: 620px;
    background: var(--card-dark);
    overflow: hidden;
    box-shadow: 0 10px 30px rgba(0,0,0,.18);
  }
  .card__accent {
    position: absolute; left: 709px; top: 0; width: 291px; height: 100%;
    background: var(--brand-orange);
  }
  .card__photo {
    position: absolute; left: 460px; top: 58px;
    width: 498px; height: 498px; border-radius: 50%;
    background: radial-gradient(circle at 45% 40%, var(--window-top) 0%, #e3d8d6 55%, var(--window-bottom) 100%);
  }
  .card__brand {
    position: absolute; left: 520px; top: 240px; width: 378px;
    text-align: center;
    font-weight: 700; font-size: 44px; line-height: 1.05;
    color: var(--logo-dark);
    text-transform: uppercase;
    letter-spacing: -0.5px;
  }
  .holder { position: absolute; left: 50px; top: 62px; }
  .holder__name {
    font-weight: 700; font-size: 37px; color: var(--brand-orange);
    letter-spacing: 0.2px;
  }
  .holder__title {
    margin-top: 2px; font-size: 25px; color: var(--text-light);
  }
  .contact-list {
    position: absolute; left: 46px; top: 181px; list-style: none;
  }
  .contact-list__item {
    display: flex; align-items: center; height: 37.5px;
    font-size: 28px; color: var(--text-light);
  }
  .contact-list__icon {
    width: 35px; height: 35px; border-radius: 50%;
    background: var(--brand-orange);
    display: flex; align-items: center; justify-content: center;
    margin-right: 8px; flex-shrink: 0;
  }
  .contact-list__note { color: var(--brand-orange); margin-left: 8px; }
  .address {
    position: absolute; left: 50px; top: 364px;
    font-size: 28px; line-height: 36px; color: var(--text-light); font-style: normal;
  }
  .website {
    position: absolute; left: 47px; top: 520px;
    font-size: 28px; color: var(--brand-orange);
  }
</style>
</head>
<body>
  <main class="card">
    <div class="card__accent"></div>
    <div class="card__photo" role="img" aria-label="Soft-focus photo of a bright office interior"></div>
    <div class="card__brand">Northfield<br>Builders Guild</div>

    <header class="holder">
      <h1 class="holder__name">DANIEL HARTWELL</h1>
      <p class="holder__title">MANAGING DIRECTOR</p>
    </header>

    <ul class="contact-list">
      <li class="contact-list__item">
        <span class="contact-list__icon">
          <svg width="20" height="20" viewBox="0 0 24 24" aria-hidden="true"><path fill="#1d1d1f" d="M6.6 10.8a15 15 0 0 0 6.6 6.6l2.2-2.2c.3-.3.7-.4 1-.2 1.1.4 2.3.6 3.6.6.6 0 1 .4 1 1V20c0 .6-.4 1-1 1A17 17 0 0 1 3 4c0-.6.4-1 1-1h3.5c.6 0 1 .4 1 1 0 1.3.2 2.5.6 3.6.1.3 0 .7-.2 1z"/></svg>
        </span>
        (555) 214-7730<span class="contact-list__note">(Office)</span>
      </li>
      <li class="contact-list__item">
        <span class="contact-list__icon">
          <svg width="18" height="20" viewBox="0 0 18 24" aria-hidden="true"><rect x="3" y="2" width="12" height="20" rx="2" fill="#1d1d1f"/><rect x="5" y="5" width="8" height="12" fill="#f7991c"/></svg>
        </span>
        800-555-0192
      </li>
      <li class="contact-list__item">
        <span class="contact-list__icon">
          <svg width="20" height="20" viewBox="0 0 24 24" aria-hidden="true"><rect x="7" y="3" width="10" height="5" fill="#1d1d1f"/><rect x="3" y="9" width="18" height="8" rx="1.5" fill="#1d1d1f"/><rect x="7" y="14" width="10" height="7" fill="#1d1d1f" stroke="#f7991c" stroke-width="1.2"/></svg>
        </span>
        555.318.0466
      </li>
      <li class="contact-list__item">
        <span class="contact-list__icon">
          <svg width="20" height="16" viewBox="0 0 24 18" aria-hidden="true"><rect x="1" y="1" width="22" height="16" fill="none" stroke="#1d1d1f" stroke-width="2"/><path d="M1 1l11 9 11-9M1 17l8-7M23 17l-8-7" fill="none" stroke="#1d1d1f" stroke-width="1.6"/></svg>
        </span>
        hello@brickwayguild.org
      </li>
    </ul>

    <address class="address">
      2450 Cedar Ridge Rd<br>
      Suite #210, Northfield<br>
      OR 97040
    </address>

    <p class="website">www.brickwayguildnetwork.org</p>
  </main>
</body>
</html>
```